Velmora Template Design for Wordpress Brightpath Site

We need graphic design and theme design work for our new site that will be running Brightpath with Velmora as the theme.

We have a draft logo that needs a graphic designer to improve it.

We are looking for sleek, modern, design that while minimal is distinct. ie page elements, content enhancement, block design that can be used, reused by in-house team.
This means there will also need to be a guide created on how to create, insert, edit each of those elements so that they can be used on new pages over time.

We have several businesses for which this is the "umbrella company" and so we will want to unify the colours and have identified a palette from which to start.

Some examples of site design we would like to stand up like:
https://www.tovrix.example/
https://pallorbranding.example/
https://business.skolvane.example/
https://www.fenwarrow.example/learning/home.aspx

When I say "coded" below, this really just means the CSS needed for page elements.

Target Market(s)

Small firms in professional services - engineers, land surveyors, consultants

Number of Pages Required

3 page

Font styles to use
Sans Serif

Requirements
Must have
• Wordpress/Velmora as base template, full home page layout with lorem ipsum placeholder
Nice to have
• custom blocks for pull quotes, call to action, a better design on the logo so it doesn't look like a rainbow.
Should not have
• Need for Structivo

```html
<!DOCTYPE html>
<html lang="en">
<head>
<meta charset="utf-8">
<title>Corvanta — Engineering, Land Surveying & Consulting</title>
<link rel="stylesheet" href="https://fonts.googleapis.com/css2?family=Fira+Sans+Condensed:wght@500;600&family=Open+Sans:wght@400;600;700&display=swap">
<style>
:root{
  --ink:#1d1d24;
  --heading:#4a4281;
  --purple:#533d8f;
  --orange:#f7941d;
  --green:#6aa84f;
  --teal:#2bb3c0;
  --soft:#eef2f6;
  --text:#4d5260;
  --muted:#8a8f9a;
  --line:#b8bcc4;
  --footer-bar:#4b4b82;
}
*{box-sizing:border-box;margin:0;padding:0}
html,body{width:1200px;height:4724px;overflow:hidden;background:#fff}
body{font-family:"Open Sans",sans-serif;color:var(--text)}
.page{position:relative;width:1200px;height:4724px;overflow:hidden}
.abs{position:absolute}
.display{font-family:"Fira Sans Condensed",sans-serif;font-weight:600;color:var(--heading);line-height:1.12}
.btn{position:absolute;display:flex;align-items:center;justify-content:center;font-size:13px;font-weight:700;color:#fff;border-radius:4px;white-space:nowrap}
.btn-green{background:var(--green)}
.btn-orange{background:var(--orange)}
.eyebrow{position:absolute;display:flex;align-items:center;gap:10px;font-size:11px;font-weight:600;color:var(--ink);letter-spacing:.2px}
.eyebrow::before{content:"";width:40px;height:5px;border-radius:3px;background:var(--orange)}
.photo{position:absolute;overflow:hidden}
.card{position:absolute;background:#fff;border-radius:10px;box-shadow:0 6px 22px rgba(40,40,80,.16)}

/* header */
.brand{position:absolute;left:110px;top:38px;display:flex;align-items:center;gap:8px;font-size:34px;font-weight:600;color:var(--ink);letter-spacing:-.5px}
.brand-dot{width:14px;height:14px;border-radius:50%;background:var(--purple)}
.nav{position:absolute;top:24px;right:113px;display:flex;align-items:center;gap:20px;font-size:12px;font-weight:600;color:var(--ink)}
.nav .btn{position:static;height:36px;padding:0 12px;font-size:12px;font-weight:600}

/* hero */
.hero-title{left:106px;top:216px;font-size:64px;line-height:1.05}
.hero-lede{left:112px;top:366px;width:420px;font-size:13px;line-height:1.6;color:var(--ink)}
.hero-photo{left:683px;top:121px;width:403px;height:532px;border-radius:28px 28px 60px 28px;background:linear-gradient(150deg,#c9ccd2 0%,#d9e7a4 45%,#e8f24a 70%,#a9a46a 100%)}
.hero-chart{left:541px;top:389px;width:285px;height:185px;padding:14px}
.tag{display:inline-block;height:12px;padding:0 7px;border-radius:6px;font-size:6px;font-weight:700;color:#fff;line-height:12px;margin-right:4px}

/* trust */
.trust-title{left:0;width:1200px;top:720px;text-align:center;font-size:21px;color:var(--heading);font-weight:400}
.badge{position:absolute;top:795px;background:#c3c6cc;opacity:.75}

/* services */
.services{position:absolute;left:0;top:961px;width:1200px;height:907px;background:var(--soft)}
.service{position:absolute;top:265px;width:312px;text-align:center}
.service .photo{position:relative;width:312px;height:436px;border-radius:0 40px 0 0}
.service h3{margin-top:24px;font-family:"Fira Sans Condensed",sans-serif;font-weight:500;font-size:29px;color:var(--heading)}
.service p{margin:10px auto 0;width:270px;font-size:13px;line-height:1.4;color:#555a66;font-weight:600}
.service .btn{position:relative;margin:22px auto 0;width:110px;height:32px;font-size:11px}

/* approach */
.center{left:0;width:1200px;text-align:center}
.intro{font-size:13px;line-height:1.7;color:#5c616c}
.approach-photo{left:110px;top:2107px;width:486px;height:671px;background:radial-gradient(circle at 45% 30%,#f2c9a4 0%,#f6a23b 35%,#c87b54 60%,#ffffff 95%)}
.step{position:absolute;left:625px;width:432px;padding-bottom:24px;border-bottom:2px solid #9aa0aa}
.step h4{font-family:"Fira Sans Condensed",sans-serif;font-weight:500;font-size:22px;color:var(--heading)}
.step p{margin-top:12px;width:360px;font-size:12px;line-height:1.55;color:#6a6f7a}

/* testimonials */
.testimonials{position:absolute;left:0;top:2778px;width:1200px;height:598px;background:var(--soft)}
.quote-card{position:absolute;top:246px;width:296px;height:220px;background:#fff;border-radius:4px;box-shadow:0 4px 14px rgba(40,40,80,.14);text-align:center}
.quote-icon{margin:26px auto 0;width:56px;height:56px;border-radius:50%;background:var(--green);display:flex;align-items:center;justify-content:center}
.quote-card p{margin:24px auto 0;width:230px;font-size:11px;line-height:1.6;color:#6a6f7a}
.stars{margin-top:12px;display:flex;justify-content:center;gap:4px}
.quote-card h5{margin-top:8px;font-size:11px;font-weight:600;color:var(--heading)}
.dots{position:absolute;top:540px;left:574px;display:flex;gap:6px}
.dots i{width:9px;height:9px;border-radius:50%;background:#3b3b44}
.dots i:first-child{background:var(--green)}

/* about */
.about-photo{left:659px;top:3450px;width:403px;height:532px;border-radius:20px 20px 60px 20px;background:linear-gradient(140deg,#6f9fae 0%,#cfd9dd 40%,#c9463e 70%,#2e3b46 100%)}
.stat-card{left:584px;top:3749px;width:277px;height:173px;padding:22px 20px}

/* cta */
.cta{position:absolute;left:0;top:4055px;width:1200px;height:305px;background:var(--purple);text-align:center;color:#fff}
.cta h2{padding-top:72px;font-family:"Fira Sans Condensed",sans-serif;font-weight:600;font-size:52px}
.cta p{margin:12px auto 0;width:860px;font-size:18px;line-height:1.3}

/* footer */
.footer-brand{position:absolute;left:106px;top:4440px;display:flex;align-items:center;gap:12px;font-size:76px;font-weight:600;color:var(--ink);letter-spacing:-2px}
.footer-brand .brand-dot{width:22px;height:22px}
.vert{position:absolute;transform:rotate(-90deg);transform-origin:left top;font-family:"Fira Sans Condensed",sans-serif;font-weight:600;font-size:23px;color:var(--heading);white-space:nowrap}
.links{position:absolute;left:561px;top:4455px;font-size:15px;line-height:22.5px;color:#555a66}
.contact{position:absolute;left:780px;top:4452px;font-size:13px;font-weight:600;color:#3b3f4a}
.contact div{display:flex;align-items:center;gap:14px;height:36px}
.copyright{position:absolute;left:0;top:4654px;width:1200px;height:70px;background:var(--footer-bar);color:#fff;font-size:10px;display:flex;align-items:center;justify-content:center}
</style>
</head>
<body>
<div class="page">

  <!-- header -->
  <div class="brand"><span>Corvanta</span><span class="brand-dot"></span></div>
  <nav class="nav">
    <span>Engineers</span><span>Land surveyors</span><span>Consultants</span>
    <span class="btn btn-orange">Get a Free Consultation</span>
  </nav>

  <!-- hero -->
  <h1 class="abs display hero-title">Built on Trust and<br>Precision</h1>
  <p class="abs hero-lede">We provide engineering, land surveying, and consulting services for infrastructure, development, and built environments.</p>
  <span class="btn btn-green" style="left:112px;top:434px;width:145px;height:36px">View Our Services</span>
  <span class="btn btn-orange" style="left:271px;top:434px;width:124px;height:36px">Start a Project</span>
  <div class="photo hero-photo" role="img" aria-label="Surveyor in a yellow hard hat and hi-vis jacket operating a total station"></div>
  <div class="card hero-chart">
    <div><span class="tag" style="background:#4a4281">ENGINEERS</span><span class="tag" style="background:var(--teal)">CONSULTANTS</span><span class="tag" style="background:var(--green)">LAND SURVEYORS</span></div>
    <svg width="257" height="140" viewBox="0 0 257 140">
      <rect x="52" y="58" width="22" height="62" fill="#f7c6d8" opacity=".6"/>
      <rect x="150" y="70" width="22" height="50" fill="#bcd2f2" opacity=".7"/>
      <rect x="40" y="10" width="40" height="14" rx="7" fill="#eceef3"/>
      <text x="46" y="21" font-size="10" font-weight="700" fill="#4a4281">98</text>
      <text x="60" y="20" font-size="5" fill="#8a8f9a">Active sites</text>
      <rect x="145" y="36" width="44" height="14" rx="7" fill="#eceef3"/>
      <text x="151" y="47" font-size="10" font-weight="700" fill="#4a4281">52</text>
      <text x="165" y="46" font-size="5" fill="#8a8f9a">Survey pts</text>
      <path d="M5 70 C20 40,35 45,50 60 S75 95,95 70 S120 40,140 70 S170 95,190 60 S225 75,250 65" fill="none" stroke="#c07ad8" stroke-width="2"/>
      <path d="M5 85 C25 75,40 90,60 80 S95 60,115 85 S150 100,170 78 S215 90,250 82" fill="none" stroke="#f08bb1" stroke-width="1.5"/>
      <path d="M5 95 C30 90,55 100,80 92 S130 85,160 96 S220 90,250 94" fill="none" stroke="#8fb3ec" stroke-width="1.5"/>
      <g font-size="5" fill="#8a8f9a"><text x="5" y="136">01</text><text x="35" y="136">02</text><text x="65" y="136">03</text><text x="95" y="136">04</text><text x="125" y="136">05</text><text x="155" y="136">06</text><text x="185" y="136">07</text><text x="215" y="136">08</text><text x="245" y="136">09</text></g>
    </svg>
  </div>

  <!-- trust -->
  <h2 class="abs trust-title">Large Brands Trust Us</h2>
  <div class="badge" style="left:120px;width:92px;height:50px;border-radius:8px"></div>
  <div class="badge" style="left:262px;width:90px;height:50px;border-radius:8px"></div>
  <div class="badge" style="left:400px;width:84px;height:50px;border-radius:8px"></div>
  <div class="badge" style="left:540px;width:84px;height:52px;border-radius:26px"></div>
  <div class="badge" style="left:678px;width:86px;height:50px;border-radius:8px"></div>
  <div class="badge" style="left:808px;width:72px;height:48px;border-radius:8px"></div>
  <div class="badge" style="left:921px;top:792px;width:66px;height:66px;border-radius:50%"></div>
  <div class="badge" style="left:1044px;top:792px;width:56px;height:56px;border-radius:50%"></div>

  <!-- services -->
  <section class="services">
    <div class="eyebrow" style="left:114px;top:62px">OUR SERVICES</div>
    <h2 class="abs display" style="left:114px;top:97px;font-size:54px">Technical Expertise. Practical<br>Execution</h2>
    <div class="service" style="left:114px">
      <div class="photo" style="border-bottom:5px solid var(--green);background:linear-gradient(160deg,#8b8f97 0%,#c7b35a 50%,#e9ecef 80%)" role="img" aria-label="Two engineers in hard hats reviewing a blueprint"></div>
      <h3>Engineering</h3>
      <p>Infrastructure engineered for longevity, compliance, and efficiency.</p>
      <span class="btn btn-orange">read more →</span>
    </div>
    <div class="service" style="left:444px">
      <div class="photo" style="border-bottom:5px solid var(--orange);background:linear-gradient(180deg,#cfd4d8 0%,#b8a88e 45%,#f07c28 70%,#6f6a66 100%)" role="img" aria-label="Land surveyor in an orange vest working with a tripod on a road"></div>
      <h3>Land Surveying</h3>
      <p>Reliable field data that forms the foundation of every successful project.</p>
      <span class="btn btn-orange">read more →</span>
    </div>
    <div class="service" style="left:773px">
      <div class="photo" style="border-bottom:5px solid var(--teal);background:linear-gradient(160deg,#d8dde2 0%,#eef1f3 45%,#c9d8e6 75%,#f3f5f7 100%)" role="img" aria-label="Consultants meeting around a table covered with charts and a laptop"></div>
      <h3>Consulting</h3>
      <p>Advisory services that reduce risk and improve decision-making.</p>
      <span class="btn btn-orange">read more →</span>
    </div>
  </section>

  <!-- approach -->
  <div class="eyebrow" style="left:528px;top:1922px">OUR APPROACH</div>
  <h2 class="abs display center" style="top:1942px;font-size:54px">Structured. Transparent. Accountable.</h2>
  <p class="abs intro center" style="top:2017px">It was popularised in the 1960s with the release of Quillmark sheets containing Lorem Ipsum passages, and more<br>recently with desktop publishing software like Pressline Composer including versions of Lorem Ipsum.</p>
  <div class="photo approach-photo" role="img" aria-label="Smiling engineer in a blue hard hat and orange vest holding a tablet"></div>
  <div class="card" style="left:296px;top:2410px;width:246px;height:94px;padding:14px">
    <svg width="218" height="66" viewBox="0 0 218 66">
      <text x="0" y="24" font-size="20" font-weight="700" fill="#4a4281">25.3</text>
      <text x="0" y="38" font-size="5" fill="#8a8f9a">Projects on time</text>
      <path d="M70 50 C85 30,95 45,110 32 S130 15,145 35 S170 10,185 30 L195 50 Z" fill="#e3b8f0" opacity=".7"/>
      <path d="M70 50 C85 38,100 48,115 40 S145 30,165 42 S185 36,195 50" fill="none" stroke="#f08bb1" stroke-width="1.5"/>
      <g font-size="6" fill="#555"><text x="78" y="64">01</text><text x="100" y="64">02</text><text x="122" y="64">03</text><text x="144" y="64">04</text><text x="166" y="64">05</text><text x="188" y="64">06</text></g>
    </svg>
  </div>
  <div class="card" style="left:348px;top:2538px;width:244px;height:140px;padding:18px">
    <svg width="208" height="104" viewBox="0 0 208 104">
      <circle cx="44" cy="52" r="40" fill="none" stroke="#d9c7f2" stroke-width="10"/>
      <circle cx="44" cy="52" r="40" fill="none" stroke="#8fb3ec" stroke-width="10" stroke-dasharray="150 260"/>
      <circle cx="44" cy="52" r="28" fill="#fff" stroke="#e4e7ee"/>
      <text x="44" y="56" font-size="14" font-weight="700" fill="#4a4281" text-anchor="middle">368</text>
      <text x="44" y="65" font-size="4" fill="#8a8f9a" text-anchor="middle">Client score</text>
      <g font-size="6" fill="#555"><rect x="130" y="10" width="34" height="10" rx="5" fill="#eceef3"/><text x="135" y="17">47 032</text><rect x="130" y="24" width="76" height="3" fill="#8fb3ec"/>
      <rect x="130" y="40" width="34" height="10" rx="5" fill="#eceef3"/><text x="135" y="47">58 405</text><rect x="130" y="54" width="66" height="3" fill="#8fb3ec"/>
      <rect x="130" y="70" width="34" height="10" rx="5" fill="#eceef3"/><text x="135" y="77">51 843</text><rect x="130" y="84" width="50" height="3" fill="#8fb3ec"/></g>
    </svg>
  </div>
  <div class="step" style="top:2203px"><h4>Clarity Before Commitment</h4><p>It was popularised in the 1960s with the release of Quillmark sheets containing Lorem Ipsum passages, and more recently with desktop publishing software</p></div>
  <div class="step" style="top:2352px"><h4>Precision in Every Detail</h4><p>It was popularised in the 1960s with the release of Quillmark sheets containing Lorem Ipsum passages, and more recently with desktop publishing software</p></div>
  <div class="step" style="top:2502px;border-bottom:0"><h4>Execution Without Surprises</h4><p>It was popularised in the 1960s with the release of Quillmark sheets containing Lorem Ipsum passages, and more recently with desktop publishing software</p></div>
  <span class="btn btn-green" style="left:625px;top:2632px;width:146px;height:35px">View Our Services</span>

  <!-- testimonials -->
  <section class="testimonials">
    <div class="eyebrow" style="left:528px;top:52px">TESTIMONIAL</div>
    <h2 class="abs display center" style="top:72px;font-size:54px">Check testimonials for our satisfied clients</h2>
    <p class="abs intro center" style="top:148px">It was popularised in the 1960s with the release of Quillmark sheets containing Lorem Ipsum passages, and more<br>recently with desktop publishing software like Pressline Composer including versions of Lorem Ipsum.</p>
    <div class="quote-card" style="left:138px">
      <div class="quote-icon"><svg width="26" height="22" viewBox="0 0 26 22"><path d="M0 22V12C0 5 4 1 10 0v4c-3 1-5 3-5 6h5v12zm14 0V12c0-7 4-11 10-12v4c-3 1-5 3-5 6h5v12z" fill="#fff"/></svg></div>
      <p>It is a long established fact that a reader will be distracted by the readable content of a page when looking at its layout.</p>
      <div class="stars"><svg width="82" height="13" viewBox="0 0 82 13"><g fill="#f7b21d"><path id="s" d="M6.5 0l2 4.2 4.5.5-3.3 3 .9 4.5-4.1-2.3-4.1 2.3.9-4.5L0 4.7l4.5-.5z"/><use href="#s" x="17"/><use href="#s" x="34"/><use href="#s" x="51"/><use href="#s" x="68"/></g></svg></div>
      <h5>Marla T. Quinby</h5>
    </div>
    <div class="quote-card" style="left:451px">
      <div class="quote-icon"><svg width="26" height="22" viewBox="0 0 26 22"><path d="M0 22V12C0 5 4 1 10 0v4c-3 1-5 3-5 6h5v12zm14 0V12c0-7 4-11 10-12v4c-3 1-5 3-5 6h5v12z" fill="#fff"/></svg></div>
      <p>It is a long established fact that a reader will be distracted by the readable content of a page when looking at its layout.</p>
      <div class="stars"><svg width="82" height="13" viewBox="0 0 82 13"><g fill="#f7b21d"><use href="#s"/><use href="#s" x="17"/><use href="#s" x="34"/><use href="#s" x="51"/><use href="#s" x="68"/></g></svg></div>
      <h5 style="font-weight:400">Marla T. Quinby</h5>
    </div>
    <div class="quote-card" style="left:765px">
      <div class="quote-icon"><svg width="26" height="22" viewBox="0 0 26 22"><path d="M0 22V12C0 5 4 1 10 0v4c-3 1-5 3-5 6h5v12zm14 0V12c0-7 4-11 10-12v4c-3 1-5 3-5 6h5v12z" fill="#fff"/></svg></div>
      <p>It is a long established fact that a reader will be distracted by the readable content of a page when looking at its layout.</p>
      <div class="stars"><svg width="82" height="13" viewBox="0 0 82 13"><g fill="#f7b21d"><use href="#s"/><use href="#s" x="17"/><use href="#s" x="34"/><use href="#s" x="51"/><use href="#s" x="68"/></g></svg></div>
      <h5 style="font-weight:400">Marla T. Quinby</h5>
    </div>
    <div class="dots"><i></i><i></i><i></i></div>
  </section>

  <!-- about -->
  <div class="eyebrow" style="left:116px;top:3463px">ABOUT US</div>
  <h2 class="abs display" style="left:116px;top:3496px;font-size:54px">Built on Expertise.</h2>
  <p class="abs" style="left:116px;top:3580px;width:480px;font-size:31px;line-height:1.1;color:var(--heading)">A professional team grounded in discipline and long-term relationships.</p>
  <p class="abs" style="left:118px;top:3705px;width:430px;font-size:12.5px;line-height:1.75;color:#5c616c">It is a long established fact that a reader will be distracted by the readable content of a page when looking at its layout. The point of using Lorem Ipsum is that it has a more-or-less normal distribution of letters, as opposed to using 'Content here, content here', making it look like readable English. Many desktop publishing</p>
  <span class="btn btn-green" style="left:116px;top:3842px;width:98px;height:36px">Read More</span>
  <div class="photo about-photo" role="img" aria-label="Two professionals smiling in an office meeting"></div>
  <div class="card stat-card">
    <svg width="237" height="130" viewBox="0 0 237 130">
      <text x="50" y="34" font-size="34" font-weight="700" fill="#2f3140" text-anchor="middle">95</text>
      <text x="50" y="46" font-size="5" fill="#6a6f7a" text-anchor="middle">COMPLETED AUDITS</text>
      <text x="50" y="53" font-size="5" fill="#6a6f7a" text-anchor="middle">THIS YEAR</text>
      <text x="180" y="34" font-size="34" font-weight="700" fill="#2f3140" text-anchor="middle">102</text>
      <text x="180" y="46" font-size="5" fill="#6a6f7a" text-anchor="middle">LICENSED STAFF</text>
      <text x="180" y="53" font-size="5" fill="#6a6f7a" text-anchor="middle">ON CALL</text>
      <g fill="#a88ae0">
        <rect x="8" y="100" width="3" height="22"/><rect x="14" y="92" width="3" height="30"/><rect x="20" y="96" width="3" height="26"/><rect x="26" y="88" width="3" height="34"/><rect x="32" y="94" width="3" height="28"/><rect x="38" y="84" width="3" height="38"/><rect x="44" y="90" width="3" height="32"/><rect x="50" y="96" width="3" height="26"/><rect x="56" y="86" width="3" height="36"/><rect x="62" y="92" width="3" height="30"/><rect x="68" y="98" width="3" height="24"/><rect x="74" y="88" width="3" height="34"/><rect x="80" y="94" width="3" height="28"/><rect x="86" y="100" width="3" height="22"/>
      </g>
      <g fill="#f08bb1"><rect x="20" y="110" width="3" height="12"/><rect x="44" y="106" width="3" height="16"/><rect x="68" y="108" width="3" height="14"/></g>
      <g fill="#8fb3ec">
        <rect x="142" y="102" width="3" height="20"/><rect x="148" y="94" width="3" height="28"/><rect x="154" y="98" width="3" height="24"/><rect x="160" y="90" width="3" height="32"/><rect x="166" y="96" width="3" height="26"/><rect x="172" y="84" width="3" height="38"/><rect x="178" y="92" width="3" height="30"/><rect x="184" y="86" width="3" height="36"/><rect x="190" y="94" width="3" height="28"/><rect x="196" y="100" width="3" height="22"/><rect x="202" y="90" width="3" height="32"/><rect x="208" y="96" width="3" height="26"/><rect x="214" y="102" width="3" height="20"/>
      </g>
    </svg>
  </div>

  <!-- cta -->
  <section class="cta">
    <h2>Built Environments. Engineered Results.</h2>
    <p>It is a long established fact that a reader will be distracted by the readable content of a page when looking at its layout. The point of using Lorem Ipsum is that it has a more-or-less</p>
    <span class="btn btn-green" style="left:427px;top:227px;width:144px;height:35px">View Our Services</span>
    <span class="btn" style="left:582px;top:227px;width:192px;height:35px;background:#43437a;font-weight:600">Get a Free Consultation</span>
  </section>

  <!-- footer -->
  <div class="footer-brand"><span>Corvanta</span><span class="brand-dot"></span></div>
  <div class="vert" style="left:515px;top:4560px">Quick Link</div>
  <div class="links">Home<br>Services<br>Engineers<br>Land Surveyors<br>Consultants</div>
  <div class="vert" style="left:738px;top:4560px">Contact Us</div>
  <div class="contact">
    <div><svg width="16" height="18" viewBox="0 0 16 18"><path d="M8 0a6.5 6.5 0 0 0-6.5 6.5C1.5 11 8 18 8 18s6.5-7 6.5-11.5A6.5 6.5 0 0 0 8 0zm0 9a2.5 2.5 0 1 1 0-5 2.5 2.5 0 0 1 0 5z" fill="#8cc63f"/></svg>48 Harlow Bend, Fairmont, OR, 97301</div>
    <div><svg width="16" height="12" viewBox="0 0 16 12"><rect width="16" height="12" rx="1.5" fill="#8cc63f"/><path d="M1 1l7 5.5L15 1" fill="none" stroke="#fff" stroke-width="1.4"/></svg>hello@corvanta.example</div>
    <div><svg width="16" height="16" viewBox="0 0 16 16"><path d="M3.6 1.2l2.2 2.6-1.3 1.8c.9 2 2.4 3.6 4.5 4.6l1.8-1.3 2.6 2.2-1.2 2.6C6.5 13.8 2 9.3 1 3.2z" fill="#8cc63f"/></svg>555-014-2278</div>
  </div>
  <div class="copyright">Copyright © 2026 corvanta.example . All rights reserved</div>

</div>
</body>
</html>
```